Cradlecraft by Lorna Business Card Design

i am starting a new business as a reborn artist (that is painting dolls to make them look like real live babies)

i eventually want to sell the dolls that i make and have classed in reborning. but at the moment i just want to get my name out there.

I do not currently have images of the dolls so cannot have an image in the design.

Non compulsory thoughts: i like the look of old wood, white and baby pink,even hot pink, and lace, denim. i had in mind something like a tiny baby in a old cradle or something, a old drawer, box, something different or unusual, it has to be a girl baby. i am also open to other thoughts on the matter. i would like plain writing not all swirly
Updates

Sorry to change but would like it to read country cradlecraft by lorna.

Industry/Entity Type

Painting

Contact Information for Business Card

Cradlecraft by Lorna
Handpainted babies that stay little
Reborn Artist Lorna Whitby
0431 756 842
marlo.t@quillbox.com

```html
<!DOCTYPE html>
<html lang="en">
<head>
<meta charset="utf-8">
<title>Cradlecraft by Lorna – Business Card</title>
<link rel="stylesheet" href="https://fonts.googleapis.com/css2?family=Tinos&display=swap">
<style>
  :root {
    --card-pink: #d65ca3;
    --text-white: #ffffff;
    --text-sky: #b3def2;
    --band-sky: #aee0f4;
    --lace-cream: #f3e3d6;
    --lace-rose: #e6a9c9;
    --portrait-light: #d9d6ee;
    --portrait-mid: #a9a7d4;
  }
  html, body {
    margin: 0;
    padding: 0;
    overflow: hidden;
  }
  .card {
    position: relative;
    width: 1200px;
    height: 740px;
    background: var(--card-pink);
    overflow: hidden;
    font-family: "Tinos", "Times New Roman", serif;
  }
  .brand-name,
  .tagline,
  .artist-name,
  .contact-line {
    position: absolute;
    left: 0;
    width: 1200px;
    margin: 0;
    text-align: center;
    font-weight: 400;
    line-height: 1;
    white-space: nowrap;
  }
  .brand-name {
    top: 52px;
    font-size: 88px;
    color: var(--text-white);
    letter-spacing: -0.5px;
  }
  .tagline {
    top: 194px;
    font-size: 39px;
    color: var(--text-white);
  }
  .artist-name {
    top: 256px;
    font-size: 38px;
    color: var(--text-sky);
  }
  .contact-line {
    top: 313px;
    font-size: 38px;
    color: var(--text-sky);
  }
  .lace-band {
    position: absolute;
    left: 0;
    top: 0;
  }
</style>
</head>
<body>
  <main class="card">
    <h1 class="brand-name">Cradlecraft by Lorna</h1>
    <p class="tagline">Handpainted babies that stay little</p>
    <p class="artist-name">Reborn Artist Lorna Whitby</p>
    <p class="contact-line">0431 756 842 marlo.t@quillbox.com</p>

    <svg class="lace-band" width="1200" height="740" viewBox="0 0 1200 740">
      <defs>
        <linearGradient id="laceFill" x1="0" y1="0" x2="0" y2="1">
          <stop offset="0" stop-color="var(--lace-cream)"/>
          <stop offset="0.5" stop-color="var(--lace-rose)"/>
          <stop offset="1" stop-color="var(--lace-cream)"/>
        </linearGradient>
        <radialGradient id="portraitFill" cx="0.5" cy="0.45" r="0.6">
          <stop offset="0" stop-color="var(--portrait-light)"/>
          <stop offset="1" stop-color="var(--portrait-mid)"/>
        </radialGradient>
      </defs>
      <rect class="band-frame" x="22" y="416" width="1154" height="152" fill="var(--band-sky)"/>
      <rect class="band-lace" x="42" y="437" width="1114" height="108" fill="url(#laceFill)"
            role="img" aria-label="Decorative pink lace leaf pattern"/>
      <ellipse class="medallion-frame" cx="617" cy="492" rx="162" ry="125" fill="var(--band-sky)"/>
      <ellipse class="medallion-portrait" cx="617" cy="490" rx="134" ry="104" fill="url(#portraitFill)"
               role="img" aria-label="Soft pencil sketch of a baby girl"/>
    </svg>
  </main>
</body>
</html>
```